The Lantern Guide

I am a life coach specializing in helping people with depression and bipolar disorder. I would like a nice, fun design for a business card.

```html
<!DOCTYPE html>
<html lang="en">
<head>
<meta charset="utf-8">
<title>The Lantern Guide – Business Card</title>
<link rel="stylesheet" href="https://fonts.googleapis.com/css2?family=Open+Sans:wght@400;600;700&display=swap">
<style>
  :root {
    --page: #e9e6e1;
    --card-black: #050608;
    --card-sheen: #2a2c30;
    --brand-blue: #2f9fdc;
    --deep-blue: #1a6fb3;
    --accent-orange: #e8693a;
    --text-white: #f2f4f6;
  }
  * { margin: 0; padding: 0; box-sizing: border-box; }
  html, body {
    width: 1200px; height: 1022px; overflow: hidden;
    background: var(--page);
    font-family: "Open Sans", Arial, sans-serif;
  }
  .canvas { position: relative; width: 1200px; height: 1022px; }
  .card {
    position: absolute; left: 100px; top: 225px;
    width: 1000px; height: 571px;
    border-radius: 28px; overflow: hidden;
    background: radial-gradient(ellipse 70% 90% at 30% 20%, var(--card-sheen) 0%, var(--card-black) 70%);
    box-shadow: 0 18px 40px rgba(0,0,0,.25);
  }
  .card-swoosh { position: absolute; inset: 0; width: 100%; height: 100%; }
  .brand-name {
    position: absolute; left: 60px; top: 208px;
    font-size: 40px; line-height: 56px; font-weight: 400; color: var(--brand-blue);
    letter-spacing: .3px; white-space: nowrap;
  }
  .divider {
    position: absolute; left: 466px; top: 92px;
    width: 2px; height: 292px; background: var(--accent-orange);
  }
  .contact-block { position: absolute; left: 496px; top: 92px; color: var(--text-white); }
  .person-name {
    font-size: 38px; font-weight: 700; color: var(--brand-blue);
    letter-spacing: 1px; line-height: 1.1;
  }
  .person-role { font-size: 19px; line-height: 1.4; margin-top: 2px; }
  .address { font-size: 19px; line-height: 1.4; margin-top: 16px; }
  .contact-list { list-style: none; margin-top: 12px; }
  .contact-list li {
    display: flex; align-items: center; gap: 11px;
    font-size: 19px; line-height: 1.5; white-space: nowrap;
  }
  .contact-list svg { width: 15px; height: 15px; flex: none; }
  .web-domain { color: var(--brand-blue); }
</style>
</head>
<body>
<div class="canvas">
  <div class="card">
    <svg class="card-swoosh" viewBox="0 0 1000 571" aria-hidden="true">
      <defs>
        <linearGradient id="blueBand" x1="0" y1="1" x2="1" y2="0">
          <stop offset="0" stop-color="#4ab8e8"/>
          <stop offset="1" stop-color="#1a6fb3"/>
        </linearGradient>
      </defs>
      <path d="M330 571 C 670 538, 925 445, 1000 300 L1000 571 Z" fill="url(#blueBand)"/>
      <path d="M270 571 C 620 530, 900 420, 1000 250" fill="none" stroke="var(--accent-orange)" stroke-width="7"/>
    </svg>

    <div class="brand-name">The Lantern Guide</div>
    <div class="divider"></div>

    <div class="contact-block">
      <h1 class="person-name">DANIEL REEVES</h1>
      <p class="person-role">Director</p>
      <p class="address">Wattle Street,<br>Glebe NSW, Australia</p>
      <ul class="contact-list">
        <li>
          <svg viewBox="0 0 16 16"><path d="M4 1 L6.5 4 L5 6 C6 8.5 7.5 10 10 11 L12 9.5 L15 12 L13 15 C7 14.5 1.5 9 1 3 Z" fill="var(--accent-orange)"/></svg>
          0407318254
        </li>
        <li>
          <svg viewBox="0 0 16 16"><rect x="4" y="1" width="8" height="14" rx="1.5" fill="none" stroke="var(--accent-orange)" stroke-width="1.8"/><circle cx="8" cy="12.5" r="1" fill="var(--accent-orange)"/></svg>
          0419652703
        </li>
        <li>
          <svg viewBox="0 0 16 16"><rect x="1" y="3" width="14" height="10" rx="1" fill="none" stroke="var(--accent-orange)" stroke-width="1.8"/><path d="M1.5 3.5 L8 9 L14.5 3.5" fill="none" stroke="var(--accent-orange)" stroke-width="1.6"/></svg>
          info@thelanternguide.com
        </li>
        <li>
          <svg viewBox="0 0 16 16"><circle cx="8" cy="8" r="6.5" fill="none" stroke="var(--accent-orange)" stroke-width="1.6"/><ellipse cx="8" cy="8" rx="2.8" ry="6.5" fill="none" stroke="var(--accent-orange)" stroke-width="1.3"/><path d="M1.5 8 H14.5" stroke="var(--accent-orange)" stroke-width="1.3"/></svg>
          <span>www.<span class="web-domain">thelanternguide</span>.com</span>
        </li>
      </ul>
    </div>
  </div>
</div>
</body>
</html>
```